Business card for new business - financial management

I need a business card designed for my new business. I'm the owner / sole trader of QVB Consulting, which provides financial management services for Government. I'd like the design to incorporate the attached business name and colours. The design should include colour and not be too way out - it needs to look at home in a government environment.
Details to be included on the card are:
QVB Consulting
Miriam Haskett
0400 386 924
miriamrhaskett@fernmail.example
47 Pallister Crescent, Curtin ACT 2605
Single or double sided designs would be good.
Employees at Australian Federal Government agencies
Government

```html
<!DOCTYPE html>
<html lang="en">
<head>
<meta charset="utf-8">
<title>QVB Consulting — Business Card</title>
<link rel="stylesheet" href="https://fonts.googleapis.com/css2?family=Open+Sans:wght@400;600;700&display=swap">
<style>
  :root {
    --backdrop: #1d1f21;
    --card-white: #ffffff;
    --band-dark: #1b5e70;
    --band-mid: #2e8aa3;
    --band-light: #9fd0dd;
    --brand-ink: #245a78;
    --contact-ink: #ffffff;
    --panel-top: #245e70;
    --panel-bottom: #143a46;
  }
  * { margin: 0; padding: 0; box-sizing: border-box; }
  html, body {
    width: 1200px;
    height: 871px;
    overflow: hidden;
    background: var(--backdrop);
  }
  .canvas {
    position: relative;
    width: 1200px;
    height: 871px;
  }
  .business-card {
    position: absolute;
    left: 150px;
    top: 178px;
    width: 900px;
    height: 514px;
    overflow: hidden;
    font-family: "Open Sans", Arial, sans-serif;
    box-shadow: 0 20px 50px rgba(0, 0, 0, 0.55);
  }
  .card-shapes {
    position: absolute;
    inset: 0;
    width: 100%;
    height: 100%;
  }
  .brand-name {
    position: absolute;
    left: 56px;
    top: 190px;
    font-size: 40px;
    font-weight: 600;
    color: var(--brand-ink);
    letter-spacing: 0.5px;
    white-space: nowrap;
  }
  .contact-block {
    position: absolute;
    left: 566px;
    top: 150px;
    color: var(--contact-ink);
  }
  .contact-name {
    font-size: 28px;
    font-weight: 700;
    margin-bottom: 28px;
    white-space: nowrap;
  }
  .contact-list {
    list-style: none;
  }
  .contact-item {
    display: flex;
    align-items: center;
    gap: 12px;
    font-size: 18px;
    line-height: 1.2;
    margin-bottom: 12px;
    white-space: nowrap;
  }
  .contact-icon {
    width: 17px;
    height: 17px;
    flex: none;
    fill: var(--contact-ink);
  }
</style>
</head>
<body>
<div class="canvas">
  <section class="business-card">
    <svg class="card-shapes" viewBox="0 0 900 514" preserveAspectRatio="none" aria-hidden="true">
      <defs>
        <linearGradient id="tealPanel" x1="0" y1="0" x2="1" y2="1">
          <stop offset="0" stop-color="var(--panel-top)"/>
          <stop offset="1" stop-color="var(--panel-bottom)"/>
        </linearGradient>
      </defs>
      <rect width="900" height="514" fill="url(#tealPanel)"/>
      <path d="M0 0 H457 C550 127 517 385 340 514 H0 Z" fill="var(--band-light)"/>
      <path d="M0 0 H437 C528 132 495 382 315 514 H0 Z" fill="var(--band-mid)"/>
      <path d="M0 0 H418 C508 136 475 381 292 514 H0 Z" fill="var(--band-dark)"/>
      <path d="M0 0 H400 C490 140 455 380 270 514 H0 Z" fill="var(--card-white)"/>
    </svg>

    <div class="brand-name">QVB Consulting</div>

    <div class="contact-block">
      <h1 class="contact-name">Miriam Haskett</h1>
      <ul class="contact-list">
        <li class="contact-item">
          <svg class="contact-icon" viewBox="0 0 24 24" aria-hidden="true"><path d="M6.6 10.8a15.1 15.1 0 0 0 6.6 6.6l2.2-2.2a1 1 0 0 1 1-.25 11.4 11.4 0 0 0 3.6.57 1 1 0 0 1 1 1V20a1 1 0 0 1-1 1A17 17 0 0 1 3 4a1 1 0 0 1 1-1h3.5a1 1 0 0 1 1 1c0 1.25.2 2.45.57 3.57a1 1 0 0 1-.25 1z"/></svg>
          <span>0400 386 924</span>
        </li>
        <li class="contact-item">
          <svg class="contact-icon" viewBox="0 0 24 24" aria-hidden="true"><path d="M2 5h20v14H2z M3.5 6.5 12 13l8.5-6.5" stroke="#1f5566" stroke-width="1.6"/></svg>
          <span>miriamrhaskett@fernmail.example</span>
        </li>
        <li class="contact-item">
          <svg class="contact-icon" viewBox="0 0 24 24" aria-hidden="true"><path d="M12 2a7 7 0 0 0-7 7c0 5.2 7 13 7 13s7-7.8 7-13a7 7 0 0 0-7-7zm0 9.5A2.5 2.5 0 1 1 12 6.5a2.5 2.5 0 0 1 0 5z"/></svg>
          <span>47 Pallister Crescent, Curtin ACT</span>
        </li>
      </ul>
    </div>
  </section>
</div>
</body>
</html>
```